Bright Steps Charity Launch Day Needs Awesome Promotion

We need promotional leaflets to promote the launch of our new charity. We want to make sure our charity starts with style. We are looking for forward thinking, clever and eye catching design that shows that we are a charity for families and professionals run by parents but that we are a professional organisation. Striking the balance between being bright and family orientated but also keeping us professional. We would like a flyer to hand out to people to advertise the launch day. Our charities mission statement and aims are below. Our strap line is Raising Expectations
We believe that everyone has the right to live their lives to the fullest of their potential. We will work together to raise expectations within the Down's syndrome community and to empower those around us to promote inclusion and achieve aspirations.
With raised expectations and empowered voices, anything is possible.
The above mission statement should be on the leaflet but the additional details below are not necessary but included to give you more information about us. If you feel it adds to the design then you can use the information.
Aims
Raising expectations of
•	The public. By educating the community and showing them how much people with Down’s syndrome can achieve we can raise expectations and change attitudes. We want to help build a community in which people with DS are not merely accepted and catered for but one in which they make meaningful positive contributions to the community. Often the community wants to help but needs the information and support to empower them to do so.
•	The parents and carers. The day of diagnosis, that moment when we stop being the public and become the parent. Many parents will never have encountered people with Down’s syndrome in their lives before, they won’t know what to expect and we want to help support, inform and train those parents to understand what their children may be able to achieve. To see past the diagnosis and to unlock the potential in their loved one.
•	The person with Down’s syndrome. If no one around us expects us to do well then the chances are we won’t. We want to empower those people caring for a person with Down’s syndrome to have high expectations and in turn pass those high expectations on to those they care for. To drive aspiration and empower people with Down’s syndrome to have high expectations of themselves.
•	Professionals. Many professionals do not have specific training in enabling a person with Down’s syndrome. We aim to raise the expectations of the professionals working with people with Down’s syndrome and their families. If they are empowered with the knowledge and skills to truly unlock potential and drive aspiration then they can go on to help so many families. Seeing that person as part of a network, part of a community, part of a family can empower people to not just treat impairments but to drive change and promote inclusion.
What we do.
•	Training. We are going to provide a range of training aimed at both parents and professionals. The training will cover many areas including but not restricted to SEN law, education, therapies, social/behaviour approaches, independent living, transition to adulthood.
•	Education and awareness. We are working with Hollowmere Saint Aldric University to run education sessions with undergraduate midwives, we are now moving on to participate with a collaborative module between all health and social care students. We will be presenting about our experiences of person centred working and team work. We hope to build on this and help provide awareness training in many settings from acute hospitals to voluntary organisations like scouting.
•	Information. Our goal is to provide pertinent information on our website and link to other useful sources. This is a work in progress and we will look to build upon this as we go. We hope to provide local advice so that each family can use the experience of the community to find the best resources and build a database of all useful local information.
•	Support. Potentially the most important aim of our charity. At every step our families need support; we aim to provide support to the families and carers so they can continue to support the person with Down’s syndrome to live life to the fullest of their potential.
Our launch day is a launch reception with refreshments, information and entertainment. It includes a family sponsored walk that is accessible to all including wheelchairs users and young children.
It is being held at
Falbrook Heath Woods Country Park
Gravesend
Kent
DA14 7QN
on Sunday 22nd May 2016
It will start at 11.00am with refreshments and walk at 12.30pm.
Contact details are
www.brightsteps-fund.org.uk
info@brightsteps-fund.org.uk
We would like people to email to register for the walk and go to the website for details. The website will be up soon but is currently under construction but has our logo etc on it for you to see. I have attached copies of logo and strap line. We would like to use these colours in the design and particularly picking out the blue.
Our charity number is 1172948 and must be included. We also need the phrase 'working in partnership with Marlow Vale Down Syndrome group but we would like this to be very small and not prominent please.
I have attached some promotional photos we have as well our logo and other information.

Updates
Just a note, the main aim of the leaflet is to sell the launch day. All the additional info about the charity was for you to understand where we are coming from. The short mission statement should be in their but not necessarily the aims and what we do bits. Include what you think really sells the launch and the sponsored walk ( including need to register). Thanks Looking forward to some awesome designs. Added Monday, March 14, 2016
Target Market(s)
families, education, health and social care professionals.
Industry/Entity Type
Charity
Requirements
Must have
- Logo
- Mission statement
- info about sponsored walk and guidance to register for this. People must register
- Date, time venue of launch day
- webpage
- charity number
- Working in partnership with Marlow Vale Down Syndrome Group. Phrase must be included but it needs to be small and inconspicuous.

Nice to have
- Some photo images of the children.

Should not have
- To much writing. It needs to be clear and concise

```html
<!DOCTYPE html>
<html lang="en">
<head>
<meta charset="utf-8">
<title>Bright Steps – Launch Day Leaflet</title>
<link rel="stylesheet" href="https://fonts.googleapis.com/css2?family=Josefin+Sans:wght@400;600;700&display=swap">
<style>
:root{
  --backdrop:#8e8e8e;
  --paper:#ffffff;
  --blue:#1a5aa6;
  --blue-tab:#3f7fc4;
  --navy:#143a6e;
  --ring:#8fb3dc;
  --green:#6cb33f;
  --lime:#9bd04a;
  --pink:#e6336b;
  --ink:#3a3a3a;
  --photo-warm:#e88a3a;
  --photo-cool:#4f86c6;
}
*{box-sizing:border-box;margin:0;padding:0}
html,body{width:1200px;height:900px;overflow:hidden}
body{background:var(--backdrop);font-family:"Josefin Sans",sans-serif;color:var(--ink);position:relative}
.page{position:absolute;top:108px;width:488px;height:687px;background:var(--paper);box-shadow:3px 4px 8px rgba(0,0,0,.35);overflow:hidden}
.page--front{left:90px}
.page--back{left:620px;width:486px}
.abs{position:absolute}
svg.art{position:absolute;left:0;top:0}

.strapline{left:12px;top:18px;color:#fff;font-size:16px;font-weight:400}
.brand{left:24px;top:268px;display:flex;align-items:center;gap:6px}
.brand__dot{width:34px;height:34px;border-radius:50%;background:var(--pink)}
.brand__name{font-size:27px;font-weight:700;color:var(--navy)}

.tab{height:23px;background:var(--blue-tab);color:#fff;font-size:19px;padding:2px 0 0 24px;border-radius:0 4px 4px 0;white-space:nowrap}
.tab--mission{left:0;top:337px;width:177px}
.tab--do{left:0;top:34px;width:178px;padding-left:30px}

.col{font-size:7.4px;line-height:1.32;text-align:justify}
.col h3{color:var(--blue);font-size:8.6px;font-weight:700;margin-top:6px}
.col .lead{font-size:11.5px;color:#222;margin-bottom:3px}
.col--f1{left:21px;top:370px;width:219px}
.col--f2{left:252px;top:349px;width:216px}

.launch{left:252px;top:462px;width:216px;height:170px;background:var(--blue);border-radius:9px;color:#fff;padding:10px 8px}
.launch__intro{font-size:7.4px;line-height:1.32}
.launch__head{color:var(--lime);font-size:12.6px;font-weight:700;margin:6px 0 5px;white-space:nowrap}
.launch__venue{display:flex;gap:6px;font-size:9px;line-height:1.25}
.launch__times{font-size:10px;line-height:1.25;margin-top:7px}
.date{left:246px;top:619px;width:222px;height:26px;background:var(--pink);color:#fff;font-size:17.5px;font-weight:700;padding:5px 0 0 8px;white-space:nowrap}
.charity-no{left:252px;top:647px;width:214px;text-align:right;font-size:7.6px;color:var(--blue)}

.footer{left:0;bottom:0;width:100%;height:30px;background:var(--green);color:#fff;display:flex;align-items:center;justify-content:space-between;padding:0 12px;font-size:9.5px;white-space:nowrap}
.footer__item{display:flex;align-items:center;gap:5px;height:16px;flex:0 0 auto}
.footer__rule{width:1px;height:16px;background:rgba(255,255,255,.8);flex:0 0 auto}

.contact{left:318px;top:10px;font-size:11px;color:var(--blue);line-height:1.45;white-space:nowrap}
.contact div{display:flex;align-items:center;gap:6px}
.col--b1{left:27px;top:70px;width:194px}
.col--b2{left:248px;top:68px;width:214px}
.col--b1 h3:first-child,.col--b2 h3:first-child{margin-top:0}

.belief{left:0;top:247px;width:100%;height:73px;background:var(--pink);color:#fff;font-size:10.3px;line-height:1.4;text-align:center;padding:12px 26px 0}
.partner{right:12px;top:324px;font-size:5.8px;color:var(--navy);white-space:nowrap}
</style>
</head>
<body>

<section class="page page--front">
  <svg class="art" width="488" height="330" viewBox="0 0 488 330" role="img" aria-label="Photo of a smiling young girl playing in a ball pit of colourful plastic balls, with an inset circle photo of a girl in glasses drawing">
    <defs>
      <linearGradient id="pitTones" x1="0" y1="0" x2="1" y2="1">
        <stop offset="0" stop-color="var(--photo-warm)"/>
        <stop offset=".55" stop-color="#d9a23d"/>
        <stop offset="1" stop-color="var(--photo-cool)"/>
      </linearGradient>
      <linearGradient id="insetTones" x1="0" y1="0" x2="1" y2="1">
        <stop offset="0" stop-color="#cfd8e6"/>
        <stop offset="1" stop-color="#6f8fbf"/>
      </linearGradient>
    </defs>
    <path d="M0 0H488V232C420 272 300 270 200 226C120 190 50 120 0 70Z" fill="url(#pitTones)"/>
    <path d="M0 70C50 120 120 190 200 226C300 270 420 272 488 232" fill="none" stroke="var(--blue)" stroke-width="5"/>
    <path d="M160 230C260 290 400 300 488 250V290C390 312 260 300 160 230Z" fill="var(--green)"/>
    <circle cx="390" cy="254" r="70" fill="url(#insetTones)" stroke="var(--ring)" stroke-width="6"/>
  </svg>
  <p class="abs strapline">Raising Expectations</p>
  <div class="abs brand"><span class="brand__dot"></span><span class="brand__name">Bright Steps</span></div>

  <h2 class="abs tab tab--mission">Our Mission:</h2>

  <div class="abs col col--f1">
    <p class="lead">Raising expectations of</p>
    <h3>The public.</h3>
    <p>By educating the community and showing them how much people with Down’s syndrome can achieve we can raise expectations and change attitudes. We want to help build a community in which people with DS are not merely accepted and catered for but one in which they make meaningful positive contributions to the community. Often the community wants to help but needs the information and support to empower them to do so.</p>
    <h3>The parents and carers.</h3>
    <p>The day of diagnosis, that moment when we stop being the public and become the parent. Many parents will never have encountered people with Down’s syndrome in their lives before, they won’t know what to expect and we want to help support, inform and train those parents to understand what their children may be able to achieve. To see past the diagnosis and to unlock the potential in their loved one.</p>
    <h3>The person with Down’s syndrome.</h3>
    <p>If no one around us expects us to do well then the chances are we won’t. We want to empower those people caring for a person with Down’s syndrome to have high expectations and in turn pass those high expectations on to those they care for. To drive aspiration and empower people with Down’s syndrome to have high expectations of themselves.</p>
  </div>

  <div class="abs col col--f2">
    <h3>Professionals.</h3>
    <p>Many professionals do not have specific training in enabling a person with Down’s syndrome. We aim to raise the expectations of the professionals working with people with Down’s syndrome and their families. If they are empowered with the knowledge and skills to truly unlock potential and drive aspiration then they can go on to help so many families. Seeing that person as part of a network, part of a community, part of a family can empower people to not just treat impairments but to drive change and promote inclusion.</p>
  </div>

  <div class="abs launch">
    <p class="launch__intro">Our launch day is a launch reception with refreshments, information and entertainment. We will then do a family sponsored walk that is accessible to all including wheelchairs users and young children.</p>
    <p class="launch__head">Our launch Day is being held at</p>
    <div class="launch__venue">
      <svg width="10" height="14" viewBox="0 0 10 14" aria-hidden="true"><path d="M5 0C2.2 0 0 2.2 0 5c0 3.6 5 9 5 9s5-5.4 5-9C10 2.2 7.8 0 5 0Zm0 7.2A2.2 2.2 0 1 1 5 2.8a2.2 2.2 0 0 1 0 4.4Z" fill="#fff"/></svg>
      <p>Falbrook Heath Woods Country Park<br>Gravesend<br>Kent<br>DA14 7QN</p>
    </div>
    <p class="launch__times">It will start at 11.00am with refreshments and walk at 12.30pm.</p>
  </div>
  <p class="abs date">Sunday 22nd May 2016</p>
  <p class="abs charity-no">Our charity number is 1172948</p>

  <footer class="abs footer">
    <span class="footer__item"><svg width="10" height="10" viewBox="0 0 24 24" aria-hidden="true"><path d="M6.6 10.8a15 15 0 0 0 6.6 6.6l2.2-2.2c.3-.3.7-.4 1-.2 1.1.4 2.3.6 3.6.6.6 0 1 .4 1 1V20c0 .6-.4 1-1 1A17 17 0 0 1 3 4c0-.6.4-1 1-1h3.5c.6 0 1 .4 1 1 0 1.3.2 2.5.6 3.6.1.3 0 .7-.2 1Z" fill="#fff"/></svg>0300-555-0142</span>
    <span class="footer__rule"></span>
    <span class="footer__item"><svg width="10" height="10" viewBox="0 0 24 24" aria-hidden="true"><circle cx="12" cy="12" r="10" fill="none" stroke="#fff" stroke-width="2"/><path d="M2 12h20M12 2c3 3 3 17 0 20M12 2c-3 3-3 17 0 20" fill="none" stroke="#fff" stroke-width="2"/></svg>www.brightsteps-fund.org.uk</span>
    <span class="footer__rule"></span>
    <span class="footer__item"><svg width="11" height="8" viewBox="0 0 24 18" aria-hidden="true"><rect width="24" height="18" rx="2" fill="#fff"/><path d="M1 1l11 9 11-9" fill="none" stroke="var(--green)" stroke-width="2"/></svg>info@brightsteps-fund.org.uk</span>
  </footer>
</section>

<section class="page page--back">
  <div class="abs contact">
    <div><svg width="11" height="11" viewBox="0 0 24 24" aria-hidden="true"><path d="M6.6 10.8a15 15 0 0 0 6.6 6.6l2.2-2.2c.3-.3.7-.4 1-.2 1.1.4 2.3.6 3.6.6.6 0 1 .4 1 1V20c0 .6-.4 1-1 1A17 17 0 0 1 3 4c0-.6.4-1 1-1h3.5c.6 0 1 .4 1 1 0 1.3.2 2.5.6 3.6.1.3 0 .7-.2 1Z" fill="var(--blue)"/></svg>0300-555-0142</div>
    <div><svg width="11" height="11" viewBox="0 0 24 24" aria-hidden="true"><circle cx="12" cy="12" r="10" fill="none" stroke="var(--blue)" stroke-width="2"/><path d="M2 12h20M12 2c3 3 3 17 0 20M12 2c-3 3-3 17 0 20" fill="none" stroke="var(--blue)" stroke-width="2"/></svg>www.brightsteps-fund.org.uk</div>
    <div><svg width="12" height="9" viewBox="0 0 24 18" aria-hidden="true"><rect width="24" height="18" rx="2" fill="var(--blue)"/><path d="M1 1l11 9 11-9" fill="none" stroke="#fff" stroke-width="2"/></svg>info@brightsteps-fund.org.uk</div>
  </div>

  <h2 class="abs tab tab--do">What we do.</h2>

  <div class="abs col col--b1">
    <h3>Training.</h3>
    <p>We are going to provide a range of training aimed at both parents and professionals. The training will cover many areas including but not restricted to SEN law, education, therapies, social/behaviour approaches, independent living, transition to adulthood.</p>
    <h3>Education and awareness.</h3>
    <p>We are working with Hollowmere Saint Aldric University to run education sessions with undergraduate midwives, we are now moving on to participate with a collaborative module between all health and social care students. We will be presenting about our experiences of person centred working and team work. We hope to build on this and help provide awareness training in many settings from acute hospitals to voluntary organisations like scouting.</p>
  </div>
  <div class="abs col col--b2">
    <h3>Information.</h3>
    <p>Our goal is to provide pertinent information on our website and link to other useful sources. This is a work in progress and we will look to build upon this as we go. We hope to provide local advice so that each family can use the experience of the community to find the best resources and build a database of all useful local information.</p>
    <h3>Support.</h3>
    <p>Potentially the most important aim of our charity. At every step our families need support; we aim to provide support to the families and carers so they can continue to support the person with Down’s syndrome to live life to the fullest of their potential.</p>
  </div>

  <p class="abs belief">We believe that everyone has the right to live their lives to the fullest of their potential. We will work together to raise expectations within the Down's syndrome community and to empower those around us to promote inclusion and achieve aspirations. With raised expectations and empowered voices, anything is possible.</p>
  <p class="abs partner">“Working in partnership with Marlow Vale Down Syndrome Group”</p>

  <svg class="abs" style="left:0;top:330px" width="486" height="357" viewBox="0 0 486 357" role="img" aria-label="Group photo of smiling children sitting together against a white brick wall, with two circle photos of children reading and a girl holding a book">
    <defs>
      <linearGradient id="groupTones" x1="0" y1="0" x2="1" y2="1">
        <stop offset="0" stop-color="#eceae4"/>
        <stop offset=".6" stop-color="#c9a9a4"/>
        <stop offset="1" stop-color="#5a6f96"/>
      </linearGradient>
      <linearGradient id="circleTones" x1="0" y1="0" x2="1" y2="1">
        <stop offset="0" stop-color="#e6e4de"/>
        <stop offset="1" stop-color="#8f9fbf"/>
      </linearGradient>
    </defs>
    <path d="M0 150C40 110 100 75 160 58V74C100 92 40 125 0 166Z" fill="var(--green)"/>
    <path d="M0 168C60 140 130 125 200 122C300 120 390 140 486 190V357H0Z" fill="url(#groupTones)"/>
    <path d="M385 140C430 180 470 240 486 330" fill="none" stroke="var(--green)" stroke-width="4"/>
    <path d="M378 132C428 170 466 230 486 300" fill="none" stroke="var(--blue)" stroke-width="3"/>
    <circle cx="210" cy="55" r="54" fill="url(#circleTones)" stroke="var(--ring)" stroke-width="6"/>
    <circle cx="334" cy="90" r="64" fill="url(#circleTones)" stroke="var(--ring)" stroke-width="6"/>
  </svg>
</section>

</body>
</html>
```